Square Business Cards for Our Restaurant / Event Venue

We need square business cards designed for the management team of our event venue and restaurant. On one side of the card should be the the Harbor Lantern 7 logo and URL www.harborlantern7.example. On the other side should be the Ember Logo and URL www.emberhall7.example. All employee details should be on the side with Ember logo. There will be a total of 5 cards to be created with the design.

Clara Bennquist
clara@harborlantern7.example

main 555.418.3072
direct 555.730.2946

4831 West Orchard Lane SE
Washington, DC 90417

Industry/Entity Type

Business

```html
<!DOCTYPE html>
<html lang="en">
<head>
<meta charset="utf-8">
<title>Ember / Harbor Lantern 7 business cards</title>
<link rel="stylesheet" href="https://fonts.googleapis.com/css2?family=Source+Sans+3:wght@400;600;700&display=swap">
<style>
  :root {
    --backdrop: #8e8e8e;
    --card-paper: #e6e6e8;
    --brand-red: #8c161d;
    --ink: #1a1a1a;
    --text-grey: #3c3c3c;
    --band-black: #0d0d0d;
    --back-web: #e9dcdc;
  }
  * { box-sizing: border-box; margin: 0; padding: 0; }
  html, body {
    width: 1105px; height: 1200px; overflow: hidden;
    background: var(--backdrop);
    font-family: "Source Sans 3", "Myriad Pro", sans-serif;
  }
  .card {
    position: absolute; left: 292px; width: 520px; height: 520px; overflow: hidden;
  }
  .card-front { top: 50px; background: var(--card-paper); }
  .card-back { top: 630px; background: var(--brand-red); }

  .brand-wordmark {
    position: absolute; right: 50px; top: 64px;
    font-size: 84px; font-weight: 700; color: var(--ink); line-height: 1;
  }
  .holder-name {
    position: absolute; left: 36px; top: 210px;
    font-size: 26px; font-weight: 700; color: var(--brand-red); line-height: 1; letter-spacing: 0.2px;
  }
  .holder-role {
    position: absolute; left: 36px; top: 244px;
    font-size: 19px; font-weight: 700; color: var(--ink); line-height: 1;
  }
  .divider {
    position: absolute; left: 38px; top: 282px; width: 436px; height: 1.5px; background: var(--ink);
  }
  .divider-accent {
    position: absolute; left: 468px; top: 276px; width: 14px; height: 14px; border-radius: 50%;
    background: var(--brand-red);
  }
  .contact-list {
    position: absolute; left: 36px; top: 304px; list-style: none;
    font-size: 18px; color: var(--text-grey); line-height: 25px;
  }
  .contact-list li { display: flex; align-items: center; gap: 9px; }
  .contact-list svg { width: 19px; height: 16px; fill: var(--brand-red); flex: none; }
  .venue-address {
    position: absolute; right: 38px; top: 398px; text-align: right; font-style: normal;
    font-size: 18px; color: var(--text-grey); line-height: 25px;
  }
  .venue-web { font-weight: 700; color: var(--brand-red); letter-spacing: 0.6px; }
  .edge-band { position: absolute; bottom: 0; height: 13px; }
  .edge-band-red { left: 0; width: 258px; background: var(--brand-red); }
  .edge-band-black { left: 262px; right: 0; background: var(--band-black); }

  .venue-badge {
    position: absolute; left: 145px; top: 120px; width: 230px; height: 230px; border-radius: 50%;
    background: var(--card-paper);
    display: flex; align-items: center; justify-content: center; text-align: center;
  }
  .venue-badge-name {
    font-size: 30px; font-weight: 400; color: var(--brand-red); line-height: 1.1;
  }
  .back-web {
    position: absolute; left: 0; right: 0; top: 412px; text-align: center;
    font-size: 17px; letter-spacing: 3.5px; color: var(--back-web);
  }
</style>
</head>
<body>
  <section class="card card-front">
    <div class="brand-wordmark">Ember</div>
    <h1 class="holder-name">CLARA BENNQUIST</h1>
    <p class="holder-role">CEO/FOUNDER</p>
    <div class="divider"></div>
    <span class="divider-accent" role="img" aria-label="Star accent"></span>
    <ul class="contact-list">
      <li><svg viewBox="0 0 20 16" aria-hidden="true"><path d="M2 5c0-3 4-4 8-4s8 1 8 4v1h-4V4.5c-1-.6-7-.6-8 0V6H2z"/><path d="M4 8h12l2 7H2z"/><circle cx="10" cy="11" r="2" fill="#e6e6e8"/></svg>555.418.3072</li>
      <li><svg viewBox="0 0 20 16" aria-hidden="true"><path d="M2 5c0-3 4-4 8-4s8 1 8 4v1h-4V4.5c-1-.6-7-.6-8 0V6H2z"/><path d="M4 8h12l2 7H2z"/><circle cx="10" cy="11" r="2" fill="#e6e6e8"/></svg>555.730.2946</li>
      <li><svg viewBox="0 0 20 16" aria-hidden="true"><path d="M1 3h18v11H1z"/><path d="M1 3l9 6 9-6" fill="none" stroke="#e6e6e8" stroke-width="1.5"/></svg>clara@harborlantern7.example</li>
    </ul>
    <address class="venue-address">
      4831 West Orchard Lane SE<br>
      Washington, DC 90417<br>
      <span class="venue-web">www.emberhall7.example</span>
    </address>
    <div class="edge-band edge-band-red"></div>
    <div class="edge-band edge-band-black"></div>
  </section>

  <section class="card card-back">
    <div class="venue-badge"><span class="venue-badge-name">Harbor<br>Lantern 7</span></div>
    <p class="back-web">www.harborlantern7.example</p>
  </section>
</body>
</html>
```